Our facebook page needs work

I want a first-rate facebook page

Target Market(s)

Computer Servers and Storage for Healthcare, Financial, Security, Surveillance, Manufacturing etc. All markets

Font styles to use
Sans Serif

Colors

Designer to choose colors to be used in the design.

Requirements
Must have
• First class look and feel
Nice to have
• creative but somewhat conservative
Should not have
• cartoons etc.

```html
<!DOCTYPE html>
<html lang="en">
<head>
<meta charset="utf-8">
<title>Vantora Technologies – Cover</title>
<link rel="stylesheet" href="https://fonts.googleapis.com/css2?family=Roboto:wght@500;700&family=Roboto+Condensed:wght@400;500&display=swap">
<style>
  :root {
    --navy: #22356b;
    --brand-blue: #2a6fc0;
    --orange: #f26f21;
    --white: #ffffff;
    --ink: #1d2a4d;
    --photo-light: #e9edf1;
    --photo-mid: #b9c4cf;
    --photo-deep: #8796a8;
  }
  * { margin: 0; padding: 0; box-sizing: border-box; }
  html, body { width: 1200px; height: 445px; overflow: hidden; background: var(--white); }
  .cover {
    position: relative;
    width: 1200px;
    height: 445px;
    overflow: hidden;
    font-family: "Roboto Condensed", "Arial Narrow", sans-serif;
    color: var(--ink);
  }
  .team-photo {
    position: absolute;
    inset: 0 400px 0 0;
    background:
      radial-gradient(ellipse at 35% 60%, var(--photo-deep) 0%, transparent 55%),
      linear-gradient(100deg, var(--photo-light) 0%, var(--photo-mid) 55%, var(--photo-light) 100%);
  }
  .frame-shape { position: absolute; inset: 0; }
  .brand {
    position: absolute;
    left: 830px;
    top: 52px;
    display: flex;
    align-items: center;
    gap: 16px;
  }
  .brand-dot {
    width: 52px; height: 52px;
    border-radius: 50%;
    background: var(--brand-blue);
  }
  .brand-name {
    font-family: "Roboto", Arial, sans-serif;
    font-weight: 700;
    font-size: 58px;
    letter-spacing: 1px;
    color: var(--brand-blue);
    line-height: 1;
  }
  .pledge {
    position: absolute;
    left: 770px;
    width: 410px;
    top: 170px;
    text-align: center;
    font-family: "Roboto", Arial, sans-serif;
    font-weight: 700;
    font-size: 20px;
    line-height: 28px;
    color: var(--navy);
    text-transform: uppercase;
  }
  .pledge-highlight { color: var(--orange); font-weight: 500; font-size: 21px; }
  .values {
    position: absolute;
    left: 770px;
    width: 410px;
    top: 290px;
    text-align: center;
    font-size: 22px;
    line-height: 30px;
    color: var(--navy);
  }
  .values-list { font-size: 21px; }
  .values-list .sep { font-size: 12px; vertical-align: middle; margin: 0 4px; }
  .contact-bar {
    position: absolute;
    left: 760px;
    right: 0;
    top: 374px;
    bottom: 0;
    background: var(--navy);
    color: var(--white);
    text-align: center;
    padding-top: 13px;
    font-size: 16px;
    line-height: 22px;
  }
</style>
</head>
<body>
<main class="cover">
  <div class="team-photo" role="img" aria-label="Photo of three colleagues in a bright office, two of them shaking hands"></div>

  <svg class="frame-shape" width="1200" height="445" viewBox="0 0 1200 445" aria-hidden="true">
    <path d="M 688 0 C 770 110 790 240 760 374 L 760 445 L 1200 445 L 1200 0 Z" fill="var(--white)"/>
    <path d="M 676 0 C 758 110 778 240 748 374 L 748 445" fill="none" stroke="var(--orange)" stroke-width="16"/>
  </svg>

  <div class="brand">
    <span class="brand-dot"></span>
    <span class="brand-name">vantora</span>
  </div>

  <p class="pledge">
    We stand behind our products<br>
    with an industy leading<br>
    <span class="pledge-highlight">5 year warranty!</span>
  </p>

  <div class="values">
    <p>Experience the Vantora Technologies</p>
    <p class="values-list">Quality <span class="sep">●</span> Reliability <span class="sep">●</span> Performance <span class="sep">●</span> Trust</p>
  </div>

  <footer class="contact-bar">
    <p>Sales 555–210–0187</p>
    <p>sales@vantorausa.com</p>
  </footer>
</main>
</body>
</html>
```